Letterhead to Introduce a 'Sister' Company.

What I am needing is a design for a letter head to introduce our current customers base of (KT Alarm) customers to our new service, 'Kestrel Tide Solar Brokers'

```html
<!DOCTYPE html>
<html lang="en">
<head>
<meta charset="utf-8">
<title>Kestrel Tide Solar Brokers – Letterhead</title>
<link rel="stylesheet" href="https://fonts.googleapis.com/css2?family=Josefin+Sans:wght@700&family=Roboto:wght@400&display=swap">
<style>
  :root {
    --backdrop: #9c9c9c;
    --paper: #ffffff;
    --navy: #134b82;
    --sun: #f7a21b;
    --contact-text: #ffffff;
  }
  html, body {
    margin: 0;
    padding: 0;
    width: 1200px;
    height: 1200px;
    overflow: hidden;
    background: var(--backdrop);
  }
  .letterhead {
    position: absolute;
    left: 192px;
    top: 102px;
    width: 816px;
    height: 996px;
    background: var(--paper);
    overflow: hidden;
  }
  .brand {
    position: absolute;
    top: 24px;
    left: 0;
    width: 100%;
    display: flex;
    flex-direction: column;
    align-items: center;
  }
  .brand-dot {
    width: 46px;
    height: 46px;
    border-radius: 50%;
    background: var(--sun);
    margin-bottom: 20px;
  }
  .brand-name {
    font-family: "Josefin Sans", sans-serif;
    font-weight: 700;
    color: var(--navy);
    text-transform: uppercase;
    text-align: center;
    line-height: 1;
  }
  .brand-name .primary {
    display: block;
    font-size: 31px;
    letter-spacing: 0.5px;
  }
  .brand-name .secondary {
    display: block;
    font-size: 14px;
    letter-spacing: 2px;
    margin-top: 6px;
  }
  .footer-bands {
    position: absolute;
    left: 0;
    top: 0;
    width: 816px;
    height: 996px;
  }
  .band-orange { fill: var(--sun); }
  .band-navy { fill: var(--navy); }
  .contact-list {
    position: absolute;
    left: 594px;
    top: 935px;
    margin: 0;
    padding: 0;
    list-style: none;
    font-family: "Roboto", sans-serif;
    font-size: 15px;
    line-height: 17.5px;
    color: var(--contact-text);
  }
  .contact-list li {
    display: flex;
    align-items: center;
    gap: 6px;
  }
  .contact-icon {
    width: 13px;
    height: 13px;
    flex: none;
  }
  .contact-icon * { fill: none; stroke: var(--contact-text); stroke-width: 1.6; }
  .contact-icon .solid { fill: var(--contact-text); stroke: none; }
</style>
</head>
<body>
  <main class="letterhead">
    <header class="brand">
      <div class="brand-dot"></div>
      <div class="brand-name">
        <span class="primary">Kestrel Tide</span>
        <span class="secondary">Solar Brokers</span>
      </div>
    </header>

    <svg class="footer-bands" viewBox="0 0 816 996" aria-hidden="true">
      <polygon class="band-orange" points="0,974 514,974 504,996 0,996"/>
      <polygon class="band-navy" points="559,920 816,920 816,996 518,996"/>
    </svg>

    <ul class="contact-list">
      <li>
        <svg class="contact-icon" viewBox="0 0 13 13" aria-hidden="true">
          <rect class="solid" x="0.5" y="2.5" width="12" height="8"/>
          <polyline points="0.5,2.5 6.5,7 12.5,2.5" style="stroke:var(--navy)"/>
        </svg>
        hello@kestreltide.com
      </li>
      <li>
        <svg class="contact-icon" viewBox="0 0 13 13" aria-hidden="true">
          <path class="solid" d="M2.5 0.8 L4.8 3.6 L3.6 5 C4.4 6.8 6 8.4 7.8 9.3 L9.3 8 L12.2 10.3 L10.6 12.3 C5.6 11.8 1.2 7.4 0.7 2.4 Z"/>
        </svg>
        2345-678-901
      </li>
      <li>
        <svg class="contact-icon" viewBox="0 0 13 13" aria-hidden="true">
          <circle cx="6.5" cy="6.5" r="5.6"/>
          <ellipse cx="6.5" cy="6.5" rx="2.4" ry="5.6"/>
          <line x1="0.9" y1="6.5" x2="12.1" y2="6.5"/>
        </svg>
        kestreltide.com
      </li>
    </ul>
  </main>
</body>
</html>
```